Home Improvements Website

I would like a website that matches our business colour scheme and uses the fonts consistent without logo. (Monserrat, Chosence & Big Noddle Tiling).
We will need numerous sections: homepage, about us, services (with tiles or links to each service - building, landscaping, decking, maintenance, roofing, gutters etc) current projects (which must be easily editable by me, who is not too tech savvy) and a contacts page with enquiry form we can link to our job management service (Tradify).

```html
<!DOCTYPE html>
<html lang="en">
<head>
<meta charset="utf-8">
<title>Verdant Yard — Home Improvements</title>
<link href="https://fonts.googleapis.com/css2?family=Montserrat:wght@500;600;700;800&family=Roboto:wght@400;500;700&display=swap" rel="stylesheet">
<style>
:root{
  --green:#45ab2b;
  --green-dark:#2f8a1b;
  --dark:#2a2524;
  --dark-2:#332e2c;
  --field:#3a3432;
  --light:#efefef;
  --text:#3b3b3b;
  --white:#ffffff;
}
*{box-sizing:border-box;margin:0;padding:0}
html,body{width:1200px;height:4428px;overflow:hidden}
body{font-family:"Roboto",sans-serif;color:var(--text);background:var(--white);position:relative}
.abs{position:absolute}
h1,h2,h3,.mont{font-family:"Montserrat",sans-serif}

/* top bar */
.topbar{left:0;top:0;width:1200px;height:38px;background:var(--dark);color:#fff;font-size:13px}
.topbar .social{left:98px;top:12px;display:flex;gap:20px}
.topbar .social span{width:12px;height:12px;border-radius:50%;background:#fff;display:block}
.topbar .phone{left:240px;top:11px;display:flex;align-items:center;gap:6px}
.topbar .mail{right:106px;top:11px;display:flex;align-items:center;gap:6px}

/* nav */
.nav{left:0;top:38px;width:1200px;height:62px;background:#fff;font-size:15px;font-family:"Roboto",sans-serif}
.nav a{position:absolute;top:22px;color:#333;text-decoration:none}
.nav a.active{color:var(--green)}
.nav .quote{top:0;left:952px;width:143px;height:62px;background:var(--green);color:#fff;display:flex;align-items:center;justify-content:center;gap:6px}
.nav .divider{position:absolute;top:0;width:1px;height:62px;background:#e2e2e2}
.brand{left:550px;top:8px;width:100px;height:122px;background:#fff;border-radius:6px;display:flex;align-items:center;justify-content:center;text-align:center;font-family:"Montserrat",sans-serif;font-weight:800;font-size:17px;line-height:1.15;color:var(--dark);z-index:5;box-shadow:0 2px 6px rgba(0,0,0,.15)}

/* hero */
.hero{left:0;top:100px;width:1200px;height:720px;background:linear-gradient(100deg,#1f2a1a 0%,#3d4f33 45%,#6c7a68 70%,#36502a 100%)}
.hero-intro{left:129px;top:204px;color:#fff;font-family:"Montserrat",sans-serif;font-weight:600;font-size:23px;line-height:31px}
.hero-title{left:129px;top:276px;color:#fff;font-family:"Montserrat",sans-serif;font-weight:700;font-size:44px;line-height:58px}
.checks{left:131px;top:404px;color:#fff;font-size:18px;list-style:none}
.checks li{display:flex;align-items:center;gap:12px;height:36px}
.btn{display:flex;align-items:center;justify-content:center;gap:10px;background:var(--green);color:#fff;font-family:"Montserrat",sans-serif;font-weight:600;font-size:16px;border-radius:2px}
.btn .arrow{width:16px;height:16px;border-radius:50%;background:#fff;display:flex;align-items:center;justify-content:center}

/* estimate */
.estimate{left:608px;top:574px;width:458px;height:564px;background:var(--dark);box-shadow:0 6px 16px rgba(0,0,0,.3);z-index:4;color:#fff}
.estimate h3{position:absolute;top:34px;width:100%;text-align:center;font-weight:800;font-size:25px}
.estimate p{position:absolute;top:68px;left:60px;width:338px;text-align:center;font-size:14px;line-height:20px}
.field{position:absolute;height:36px;border:1px solid #5a5452;background:var(--field);font-size:13px;padding:0 16px;display:flex;align-items:center;font-family:"Montserrat",sans-serif;font-weight:500}
.field.area{align-items:flex-start;padding-top:16px}
.field .caret{position:absolute;right:-1px;top:-1px;width:44px;height:36px;background:var(--green);display:flex;align-items:center;justify-content:center}

/* about */
.about-title{left:129px;top:926px;font-size:45px;font-weight:800;color:var(--dark)}
.green{color:var(--green)}
.about-text{left:129px;top:986px;width:450px;font-size:17px;line-height:29px;color:#444}

/* services */
.section-title{width:1200px;left:0;text-align:center;font-size:45px;font-weight:800;color:var(--dark)}
.dark-band{left:0;top:1520px;width:1200px;height:740px}
.hex{position:absolute;clip-path:polygon(50% 0,100% 25%,100% 75%,50% 100%,0 75%,0 25%);background:var(--green)}
.hex .ring{position:absolute;inset:7px;clip-path:inherit;background:#fff}
.hex .photo{position:absolute;inset:14px;clip-path:polygon(50% 0,100% 25%,100% 75%,50% 100%,0 75%,0 25%)}
.hex .label{position:absolute;width:100%;text-align:center;color:#fff;font-family:"Montserrat",sans-serif;font-weight:700;text-shadow:0 1px 3px rgba(0,0,0,.6)}

.why-title{top:1770px;color:#fff}
.why-sub{left:0;width:1200px;top:1852px;text-align:center;color:#ddd;font-size:17px;line-height:31px}
.why-item{position:absolute;top:1930px;width:240px;text-align:center;color:#fff;font-size:21px}
.why-item svg{display:block;margin:0 auto 12px}

/* work */
.tile{position:absolute}
.view-more{display:flex;flex-direction:column;align-items:center;justify-content:center;background:rgba(58,160,60,.9);color:#fff;font-family:"Montserrat",sans-serif;font-weight:600;font-size:27px;gap:18px}
.view-more .dot{width:36px;height:36px;border-radius:50%;background:#fff;display:flex;align-items:center;justify-content:center}

/* process */
.process{left:0;top:3163px;width:1200px;height:485px;background:var(--light)}
.eyebrow{left:129px;top:3244px;font-size:14px;font-weight:700;color:var(--green);font-family:"Montserrat",sans-serif}
.process-title{left:129px;top:3272px;font-size:32px;line-height:39px;font-weight:800;color:var(--dark)}
.process-text{left:129px;top:3412px;width:380px;font-size:14px;line-height:24px;color:#333}
.step-icon{position:absolute;left:608px;width:52px;height:48px;display:flex;align-items:center;justify-content:center}
.step{position:absolute;left:681px;width:394px;border-bottom:1px solid #9a9a9a;padding-bottom:4px}
.step small{display:block;font-size:13px;color:#333}
.step b{display:block;font-family:"Montserrat",sans-serif;font-weight:700;font-size:21px;color:var(--dark)}
.step .toggle{position:absolute;right:4px;top:14px}
.step-desc{left:681px;top:3318px;width:392px;font-size:12px;line-height:21px;color:#333}

/* cta */
.cta{left:0;top:3648px;width:1200px;height:430px;background:linear-gradient(180deg,#233021 0%,#2f4a27 50%,#3a5a2d 100%)}
.cta-title{left:0;top:3734px;width:1200px;text-align:center;color:#fff;font-size:30px;line-height:46px;font-weight:800;letter-spacing:-.5px}

/* footer */
.footer-links{list-style:none;font-family:"Montserrat",sans-serif;font-weight:700;font-size:13px;color:#fff}
.footer-col{font-size:13px;color:#fff}
.footer-col h4{font-family:"Montserrat",sans-serif;font-weight:700;font-size:13px;margin-bottom:12px}
.footer-col a{display:block;color:#fff;text-decoration:underline;margin-bottom:11px}
.fsocial{position:absolute;width:32px;height:32px;border:1.5px solid #bbb;border-radius:50%}
.copyright{left:0;top:4384px;width:1200px;text-align:center;color:#ccc;font-size:14px}
</style>
</head>
<body>

<!-- top bar -->
<div class="abs topbar">
  <div class="abs social"><span></span><span></span><span></span></div>
  <div class="abs phone">
    <svg width="11" height="11" viewBox="0 0 24 24"><path fill="#fff" d="M6.6 10.8a15.1 15.1 0 0 0 6.6 6.6l2.2-2.2a1 1 0 0 1 1-.25 11.4 11.4 0 0 0 3.6.57 1 1 0 0 1 1 1V20a1 1 0 0 1-1 1A17 17 0 0 1 3 4a1 1 0 0 1 1-1h3.5a1 1 0 0 1 1 1c0 1.25.2 2.45.57 3.57a1 1 0 0 1-.25 1z"/></svg>
    +1 555 010 2040
  </div>
  <div class="abs mail">
    <svg width="12" height="9" viewBox="0 0 24 18"><path fill="#fff" d="M0 0h24v18H0z"/><path fill="none" stroke="#2a2524" stroke-width="2" d="M1 1l11 9 11-9"/></svg>
    info@verdantyard.com
  </div>
</div>

<!-- nav -->
<nav class="abs nav">
  <a class="active" style="left:101px">Home</a>
  <span class="divider" style="left:167px"></span>
  <a style="left:191px">About Us</a>
  <span class="divider" style="left:278px"></span>
  <a style="left:304px">Services</a>
  <a style="left:772px">Projects</a>
  <span class="divider" style="left:853px"></span>
  <a style="left:878px">Contact</a>
  <a class="quote"><svg width="16" height="16" viewBox="0 0 24 24" fill="none" stroke="#fff" stroke-width="2"><path d="M11 4H4v16h16v-7"/><path d="M18 2l4 4-10 10H8v-4z"/></svg>Get A Quote</a>
</nav>
<div class="abs brand">VERDANT<br>YARD</div>

<!-- hero -->
<div class="abs hero" role="img" aria-label="Photo of a suburban house with a landscaped front lawn and trees"></div>
<div class="abs hero-intro">we have a wealth of<br>knowledge and experience in the</div>
<h1 class="abs hero-title">Landscaping and<br>Construction Industries</h1>
<ul class="abs checks">
  <li><svg width="22" height="22" viewBox="0 0 24 24" fill="none" stroke="#fff" stroke-width="1.8"><path d="M21 11.1V12a9 9 0 1 1-5.3-8.2"/><path d="M22 4 12 14l-3-3"/></svg>25 Years Combined Experience</li>
  <li><svg width="22" height="22" viewBox="0 0 24 24" fill="none" stroke="#fff" stroke-width="1.8"><path d="M21 11.1V12a9 9 0 1 1-5.3-8.2"/><path d="M22 4 12 14l-3-3"/></svg>Extraordinary driveway and garden installation</li>
  <li><svg width="22" height="22" viewBox="0 0 24 24" fill="none" stroke="#fff" stroke-width="1.8"><path d="M21 11.1V12a9 9 0 1 1-5.3-8.2"/><path d="M22 4 12 14l-3-3"/></svg>Quality that is guaranteed</li>
</ul>
<a class="abs btn" style="left:132px;top:540px;width:188px;height:50px">GET STARTED <span class="arrow"><svg width="8" height="8" viewBox="0 0 10 10"><path d="M3 1l4 4-4 4" fill="none" stroke="#45ab2b" stroke-width="2"/></svg></span></a>

<svg class="abs" style="left:0;top:640px" width="1200" height="190" viewBox="0 0 1200 190">
  <polygon points="0,20 600,160 1200,40 1200,190 0,190" fill="#2a2524"/>
  <polygon points="0,42 600,175 1200,58 1200,190 0,190" fill="#fff"/>
  <polygon points="0,30 250,88 230,96 0,42" fill="#fff" opacity="0"/>
</svg>

<!-- estimate form -->
<form class="abs estimate">
  <h3 class="mont">GET A FREE ESTIMATE</h3>
  <p>Fill out our form below and a representative will be in touch.</p>
  <div class="field" style="left:25px;top:136px;width:196px">NAME</div>
  <div class="field" style="left:237px;top:136px;width:196px">PHONE</div>
  <div class="field" style="left:25px;top:191px;width:196px">EMAIL</div>
  <div class="field" style="left:237px;top:191px;width:196px">ADDRESS</div>
  <div class="field" style="left:25px;top:244px;width:408px">ESTIMATE TYPE
    <span class="caret"><svg width="14" height="8" viewBox="0 0 14 8"><path d="M0 0h14L7 8z" fill="#fff"/></svg></span>
  </div>
  <div class="field area" style="left:25px;top:299px;width:408px;height:110px">HOW CAN WE HELP ?</div>
  <span class="btn" style="position:absolute;left:192px;top:425px;width:241px;height:45px">START MY ESTIMATE <span class="arrow"><svg width="8" height="8" viewBox="0 0 10 10"><path d="M3 1l4 4-4 4" fill="none" stroke="#45ab2b" stroke-width="2"/></svg></span></span>
</form>

<!-- about -->
<h2 class="abs about-title">ABOUT <span class="green">VERDANT</span></h2>
<p class="abs about-text">Lorem Ipsum is simply dummy text of the printing and typesetting industry. Lorem Ipsum has been the industry's standard dummy text ever since the 1500s, when an unknown printer took a galley of type and scrambled it to make a type specimen book. It has survived not only five</p>

<!-- services -->
<h2 class="abs section-title" style="top:1262px">OUR <span class="green">SERVICES</span></h2>
<svg class="abs dark-band" viewBox="0 0 1200 740" width="1200" height="740">
  <polygon points="0,44 600,-10 1200,44 1200,680 0,740" fill="#332d2b"/>
  <polyline points="0,44 600,-10 1200,44" fill="none" stroke="#45ab2b" stroke-width="8"/>
</svg>
<div class="abs" style="left:0;top:1560px;width:1200px;height:680px;background:linear-gradient(180deg,rgba(70,58,52,.5),rgba(40,34,32,.2))" role="img" aria-label="Dark wooden fence texture background"></div>

<div class="hex" style="left:191px;top:1379px;width:240px;height:276px">
  <div class="ring"></div>
  <div class="photo" role="img" aria-label="Photo of a timber deck with patio furniture" style="background:linear-gradient(180deg,#4a4a48 0%,#8f7f6a 55%,#b09a7e 100%)"></div>
  <div class="label" style="top:184px;font-size:18px">DECKING</div>
</div>
<div class="hex" style="left:450px;top:1346px;width:300px;height:344px">
  <div class="ring"></div>
  <div class="photo" role="img" aria-label="Photo of a landscaped garden with lawn and stepping stones" style="background:linear-gradient(180deg,#6b4a36 0%,#5b7a3a 45%,#3f9a2e 100%)"></div>
  <div class="label" style="top:232px;font-size:21px">LANDSCAPING</div>
</div>
<div class="hex" style="left:767px;top:1379px;width:240px;height:276px">
  <div class="ring"></div>
  <div class="photo" role="img" aria-label="Photo of a roofer laying roof tiles" style="background:linear-gradient(180deg,#6d7270 0%,#8d8f8c 50%,#5f6461 100%)"></div>
  <div class="label" style="top:184px;font-size:18px">ROOFING</div>
</div>

<h2 class="abs section-title why-title">WHY CHOOSE US?</h2>
<p class="abs why-sub">We understand how important your home is to you and work wirth you<br>to ensure you get the results you want.</p>

<div class="why-item" style="left:191px">
  <svg width="96" height="108" viewBox="0 0 96 108"><polygon points="48,3 93,28 93,80 48,105 3,80 3,28" fill="none" stroke="#fff" stroke-width="2.5"/><circle cx="54" cy="46" r="14" fill="#45ab2b"/><path d="M44 56 28 72" stroke="#fff" stroke-width="5" stroke-linecap="round"/><circle cx="54" cy="46" r="6" fill="none" stroke="#fff" stroke-width="2.5"/></svg>
  Professionalism
</div>
<div class="why-item" style="left:487px">
  <svg width="96" height="108" viewBox="0 0 96 108"><polygon points="48,3 93,28 93,80 48,105 3,80 3,28" fill="none" stroke="#fff" stroke-width="2.5"/><circle cx="48" cy="54" r="22" fill="#45ab2b"/><path d="M37 54l8 8 16-18" fill="none" stroke="#fff" stroke-width="4"/></svg>
  Better Results
</div>
<div class="why-item" style="left:767px">
  <svg width="96" height="108" viewBox="0 0 96 108"><polygon points="48,3 93,28 93,80 48,105 3,80 3,28" fill="none" stroke="#fff" stroke-width="2.5"/><circle cx="34" cy="38" r="5" fill="#45ab2b"/><circle cx="62" cy="38" r="5" fill="#45ab2b"/><circle cx="34" cy="70" r="5" fill="#45ab2b"/><circle cx="62" cy="70" r="5" fill="#45ab2b"/><path d="M39 38h18M62 43v5a6 6 0 0 1-6 6H40a6 6 0 0 0-6 6v5M39 70h18" fill="none" stroke="#fff" stroke-width="2.5"/></svg>
  Quality Work
</div>

<!-- latest work -->
<h2 class="abs section-title" style="top:2350px">LATEST <span class="green">WORK</span></h2>
<div class="tile" style="left:137px;top:2448px;width:456px;height:268px;background:linear-gradient(120deg,#7a5a44 0%,#4f8a2e 45%,#a7a49e 100%)" role="img" aria-label="Photo of a new lawn with timber sleeper edging and paving"></div>
<div class="tile" style="left:602px;top:2448px;width:457px;height:268px;background:linear-gradient(180deg,#c9c8c4 0%,#8e7d6f 55%,#9c8877 100%)" role="img" aria-label="Photo of a block-paved driveway in front of a house"></div>
<div class="tile" style="left:137px;top:2726px;width:301px;height:269px;background:linear-gradient(180deg,#7a5c42 0%,#4e8a2c 60%,#9e9c96 100%)" role="img" aria-label="Photo of timber garden steps beside artificial grass"></div>
<div class="tile view-more" style="left:447px;top:2726px;width:301px;height:269px">
  <span class="dot"><svg width="14" height="14" viewBox="0 0 24 24" fill="none" stroke="#45ab2b" stroke-width="2"><path d="M14 3h7v7M21 3l-9 9M10 5H4v15h15v-6"/></svg></span>
  View More
</div>
<div class="tile" style="left:758px;top:2726px;width:301px;height:269px;background:linear-gradient(180deg,#9bb4c9 0%,#a07a52 40%,#8a6a45 65%,#4f9a33 100%)" role="img" aria-label="Photo of a new timber fence along a lawn"></div>
<a class="abs btn" style="left:504px;top:3034px;width:187px;height:48px;font-size:15px">LEARN MORE <span class="arrow"><svg width="8" height="8" viewBox="0 0 10 10"><path d="M3 1l4 4-4 4" fill="none" stroke="#45ab2b" stroke-width="2"/></svg></span></a>

<!-- process -->
<div class="abs process"></div>
<div class="abs eyebrow">OUR PROCESS</div>
<h2 class="abs process-title">A COMPANY YOU CAN<br>TRUST TO BE WITH YOU<br>AT EVERY STEP</h2>
<p class="abs process-text">We don't sub-contract any of our work out and only have one job running at a time. This means the quality of every job is at its maximum leavel and your job has our full attention.</p>

<div class="step-icon" style="top:3249px;background:var(--green)"><svg width="26" height="26" viewBox="0 0 24 24" fill="none" stroke="#fff" stroke-width="1.6"><path d="M4 20 20 4M14 4h6v6M4 14l6 6"/></svg></div>
<div class="step" style="top:3250px"><small>STEP 1</small><b>CONTACT</b>
  <svg class="toggle" width="16" height="16" viewBox="0 0 16 16"><path d="M2 2l12 12M14 2 2 14" stroke="#45ab2b" stroke-width="1.8"/></svg></div>
<p class="abs step-desc">Fill out our contact form or give us a call to beging your FREE service estimate. Lorem Ipsum is simply dummy text of the printing and typesetting industry. Lorem Ipsum has been the industry's standard dummy text ever since the 1500s.</p>

<div class="step-icon" style="top:3438px;background:var(--dark)"><svg width="22" height="26" viewBox="0 0 22 26" fill="none" stroke="#fff" stroke-width="1.6"><path d="M2 1h12l6 6v18H2z M6 12h10M6 16h10M6 20h7"/></svg></div>
<div class="step" style="top:3436px"><small>STEP 2</small><b>PROPOSAL</b>
  <svg class="toggle" width="18" height="18" viewBox="0 0 18 18"><path d="M9 0v18M0 9h18" stroke="#45ab2b" stroke-width="1.8"/></svg></div>

<div class="step-icon" style="top:3508px;background:var(--dark)"><svg width="26" height="24" viewBox="0 0 26 24" fill="none" stroke="#fff" stroke-width="1.6"><path d="M2 22h22M5 22V10l8-7 8 7v12M10 22v-6h6v6"/></svg></div>
<div class="step" style="top:3507px"><small>STEP3</small><b>CONSTRUCTION</b>
  <svg class="toggle" width="18" height="18" viewBox="0 0 18 18"><path d="M9 0v18M0 9h18" stroke="#45ab2b" stroke-width="1.8"/></svg></div>

<!-- cta -->
<div class="abs cta" role="img" aria-label="Photo of a curved garden path through a lawn at dusk"></div>
<h2 class="abs cta-title">WE TAKE CARE OF YOUR LANDSCAPE.<br>YOU TAKE BACK YOUR FREE TIME.</h2>
<a class="abs btn" style="left:480px;top:3845px;width:240px;height:45px;font-size:15px">START MY ESTIMATE <span class="arrow"><svg width="8" height="8" viewBox="0 0 10 10"><path d="M3 1l4 4-4 4" fill="none" stroke="#45ab2b" stroke-width="2"/></svg></span></a>

<!-- footer -->
<svg class="abs" style="left:0;top:3950px" width="1200" height="478" viewBox="0 0 1200 478">
  <polygon points="0,122 600,18 1200,122 1200,478 0,478" fill="#2a2524"/>
  <polyline points="0,122 600,14 1200,122" fill="none" stroke="#45ab2b" stroke-width="8"/>
</svg>
<div class="abs mont" style="left:193px;top:4180px;width:116px;text-align:center;color:#fff;font-weight:800;font-size:20px;line-height:24px">VERDANT<br>YARD</div>

<ul class="abs footer-links" style="left:385px;top:4150px;line-height:35px">
  <li>HOME</li><li>ABOUT US</li><li>PROJECTS</li><li>CONTACT</li>
</ul>
<div class="abs footer-col" style="left:504px;top:4148px">
  <h4>SERVICES</h4><a>Building</a><a>Landscaping</a><a>Decking</a>
</div>
<div class="abs footer-col" style="left:633px;top:4148px">
  <h4>SERVICES</h4><a>Maintenance</a><a>Roofing</a><a>Gutters</a>
</div>
<div class="abs" style="left:786px;top:4148px;width:282px;height:110px;background:linear-gradient(135deg,#e7eef2,#d6e2ea);border:2px solid #c9a35a" role="img" aria-label="Map showing the company location"></div>
<svg class="abs" style="left:920px;top:4185px" width="16" height="22" viewBox="0 0 16 22"><path d="M8 0a8 8 0 0 1 8 8c0 6-8 14-8 14S0 14 0 8a8 8 0 0 1 8-8z" fill="#e23b3b"/><circle cx="8" cy="8" r="3" fill="#fff"/></svg>

<span class="fsocial" style="left:525px;top:4306px"></span>
<span class="fsocial" style="left:565px;top:4306px"></span>
<span class="fsocial" style="left:603px;top:4306px"></span>
<span class="fsocial" style="left:642px;top:4306px"></span>
<div class="abs" style="left:29px;top:4363px;width:1142px;height:1px;background:#4a4442"></div>
<div class="abs copyright">© 2024 Verdant Yard. All Rights are Reserved.</div>

</body>
</html>
```